Simply Sugar Bloom Buisness Card

I would like a Buisness card and matching letterhead for my small but personal hobby/buisness.
Something elegant, professional and pretty.
I mainly do wedding cakes in our small rural area. But also do occasion cakes, cupcakes, cookies and catering events.
I am thinking something subtle, vintage, scrolls, lace, damask, nothing too wow or out there. But open to any suggestions.

Industry/Entity Type

Catering

Contact Information for Business Card

Simply Sugar Bloom
abn: 41 503 917 248
Marnie Holloway
Wattle Creek
t: 0491 352 806
e: sugarbloomcakes@pastrymail.example

Logo Text

Simply Sugar Bloom

Logo styles of interest
Wordmark Logo
Requirements
Must have
• Elegance and class
Should not have
• Should not have Hearts or Bows

```html
<!DOCTYPE html>
<html lang="en">
<head>
<meta charset="utf-8">
<title>Simply Sugar Bloom – Business Card</title>
<link rel="stylesheet" href="https://fonts.googleapis.com/css2?family=Cinzel:wght@500&family=Open+Sans:wght@400;500&display=swap">
<style>
  :root {
    --page-bg: #f2f2f2;
    --card-black: #121212;
    --damask-dark: #0c0c0c;
    --damask-mid: #262626;
    --band-black: #0a0a0a;
    --gold: #e2b23a;
    --gold-deep: #b07d1c;
    --gold-line: #9a7a3a;
    --white: #ffffff;
  }
  * { box-sizing: border-box; margin: 0; padding: 0; }
  html, body {
    width: 1200px; height: 900px; overflow: hidden;
    background: var(--page-bg);
  }
  .business-card {
    position: absolute; left: 100px; top: 164px;
    width: 1000px; height: 572px;
    border-radius: 34px; overflow: hidden;
    background: var(--card-black);
    box-shadow: 0 18px 40px rgba(0,0,0,0.25);
  }
  .damask-field {
    position: absolute; inset: 0;
    background: radial-gradient(ellipse at 50% 45%, var(--damask-mid) 0%, var(--damask-dark) 75%);
  }
  .name-band {
    position: absolute; left: 0; right: 0; top: 212px; height: 92px;
    background: var(--band-black);
    border-top: 2px solid var(--gold-line);
    border-bottom: 2px solid var(--gold-line);
  }
  .wordmark {
    position: absolute; left: 0; right: 0; top: 212px; height: 92px;
    display: flex; align-items: center; justify-content: center;
    font-family: "Cinzel", serif; font-weight: 500;
    font-size: 58px; color: var(--white); letter-spacing: 1px;
  }
  .ornament {
    position: absolute; left: 390px; width: 220px;
    background: radial-gradient(ellipse at center, var(--gold) 0%, var(--gold-deep) 45%, rgba(176,125,28,0) 72%);
  }
  .ornament--top { top: 66px; height: 136px; }
  .ornament--bottom { top: 314px; height: 132px; }
  .owner {
    position: absolute; right: 52px; top: 50px; text-align: right;
    font-family: "Open Sans", sans-serif; font-size: 24px; line-height: 1.45;
    color: var(--gold);
  }
  .contact {
    position: absolute; left: 52px; top: 428px;
    font-family: "Open Sans", sans-serif; color: var(--white);
  }
  .contact-line { display: flex; align-items: center; gap: 12px; font-size: 30px; line-height: 44px; }
  .contact-icon { width: 30px; height: 30px; flex: none; }
  .contact-abn { font-size: 22px; padding-left: 42px; line-height: 30px; }
</style>
</head>
<body>
  <div class="business-card">
    <div class="damask-field" role="img" aria-label="Dark black damask scroll pattern covering the card"></div>
    <div class="ornament ornament--top" role="img" aria-label="Gold baroque scroll ornament above the name"></div>
    <div class="name-band"></div>
    <div class="wordmark">Simply Sugar Bloom</div>
    <div class="ornament ornament--bottom" role="img" aria-label="Gold baroque scroll ornament below the name"></div>

    <div class="owner">
      <p>Marnie Holloway</p>
      <p>Wattle Creek</p>
    </div>

    <div class="contact">
      <p class="contact-line">
        <svg class="contact-icon" viewBox="0 0 24 24" aria-hidden="true">
          <path fill="#e2b23a" d="M6.6 10.8a15.1 15.1 0 0 0 6.6 6.6l2.2-2.2a1 1 0 0 1 1-.25 11.4 11.4 0 0 0 3.6.57 1 1 0 0 1 1 1V20a1 1 0 0 1-1 1A17 17 0 0 1 3 4a1 1 0 0 1 1-1h3.5a1 1 0 0 1 1 1c0 1.25.2 2.46.57 3.6a1 1 0 0 1-.25 1z"/>
        </svg>
        0491 352 806
      </p>
      <p class="contact-line">
        <svg class="contact-icon" viewBox="0 0 24 24" aria-hidden="true">
          <rect x="2" y="5" width="20" height="14" rx="1.5" fill="#e2b23a"/>
          <path d="M3 6.5l9 6.5 9-6.5" fill="none" stroke="#121212" stroke-width="1.6"/>
        </svg>
        sugarbloomcakes@pastrymail.example
      </p>
      <p class="contact-abn">abn: 41 503 917 248</p>
    </div>
  </div>
</body>
</html>
```